Letterhead Design for Vostrand Corporate Stationery

We are seeking a talented designer on ArtHive to create a professional and cohesive corporate stationery set for our company, Vostrand. Vostrand is a prominent player in the Commercial Real Estate industry, and we need stationery that reflects our brand's excellence and professionalism.

Scope of Work:

1. Letterhead Template (Microsoft Word):

Design a letterhead template in Microsoft Word format that adheres to our brand standards (attached in project files).
Include all necessary elements such as company logo, address, contact information, and any other relevant details.
The letterhead should be clean, elegant, and suitable for official business correspondence.

2. Business Cards:

Design business cards for our team members using the provided brand guidelines.
Include name, title, contact information, and the Vostrand logo.
Create a design that leaves a lasting impression and reflects our brand's professionalism.

3. Envelopes:

Design envelopes in various sizes (e.g., standard letter and legal sizes) that match the overall stationery theme.
Ensure that the design includes our company name, logo, and return address in accordance with brand guidelines.

4. Stationery:

Create a visually appealing stationery template that can be used for various documents and correspondence.
Ensure that the stationery design aligns with our brand standards and maintains consistency across all materials.

Submission Requirements:

Provide high-resolution files for each item (letterhead, business cards, envelopes, and stationery) in formats suitable for both print and digital use.
Include editable source files (e.g., Adobe Illustrator, Photoshop) for future modifications if necessary.

Design Guidelines:

Our brand is known for professionalism, trustworthiness, and excellence in the Commercial Real Estate industry. Please adhere to the brand standards provided in the project attachments.
Use our company colors, fonts, and logo as specified in the brand guidelines.
Feel free to be creative within the boundaries of our brand to make our stationery stand out while maintaining a professional look.

Budget and Timeline:

We are looking for high-quality designs at a competitive price.
The project timeline is flexible, but we would appreciate prompt responses from designers.
Please submit your best pricing and estimated delivery times with your proposals.
We look forward to receiving your creative and professional designs that will represent Vostrand in the best possible light. Thank you for considering our project, and we can't wait to see your submissions on ArtHive!

Target Market(s)

Our primary target market for the corporate stationery design project includes, but is not limited to: Investors: Individuals or entities interested in commercial real estate investment opportunities. Brokers: Commercial real estate brokers who facilitate property transactions and negotiations. Tenant Representatives: Professionals who advocate for the interests of tenants in commercial lease transactions. Lenders: Financial institutions and lenders involved in providing financing for commercial real estate projects. Property Owners: Owners of commercial real estate properties seeking professional correspondence materials. Industry Partners: Professionals and organizations within the commercial real estate industry who collaborate with or provide services to Vostrand. Prospective Clients: Potential clients or partners exploring opportunities in the commercial real estate sector. Please note that while these are the primary target market segments, the stationery design should also appeal to a broader audience within the commercial real estate industry and convey professionalism and trustworthiness to all stakeholders.

Industry/Entity Type

Commercial Real Estate

Font styles to use
Sans Serif

Colors
0054AA
0677BA
7BADD7
CADEEF
E8F1F8
0094D4
00A9DD
6FCCEA
C7EBF8
E9F6FB
F0912C
F2A743
F7CA91
FBE8D2
FDF5EE
EE7325
F08F49
F5BC92
FAE3D3
FDF4ED

Requirements
Must have
• Brand Consistency: Ensure that the design adheres to Vostrand's existing brand standards and guidelines (provided in project attachments). Professional Appearance: The stationery must convey professionalism, trustworthiness, and excellence in the Commercial Real Estate industry. Logo Usage: Integrate the Vostrand logo prominently and appropriately on all stationery items. Contact Information: Include accurate contact details, such as the company's address, phone number, email address, and website URL. Typography: Use the specified fonts from the brand guidelines for all text elements, maintaining consistency in font style and size. Color Palette: Utilize the designated brand colors consistently throughout the design. File Formats: Ensure that the final design files are provided in high-resolution formats suitable for both print and digital use. Also, request editable source files (e.g., Adobe Illustrator, Photoshop) for future modifications if needed. Print-Ready: Prepare the design files to be print-ready, including the appropriate bleed and margin specifications for printing purposes. Stationery Variations: Include designs for letterhead, business cards, envelopes (multiple sizes if applicable), and general stationery. Creativity within Brand Guidelines: Encourage designers to be creative while working within the boundaries of Vostrand's brand standards, making the stationery unique and eye-catching. Versatility: Ensure that the stationery can be easily adapted for various purposes, such as formal business correspondence, presentations, and more. Timely Delivery: Specify your preferred timeline for receiving initial design concepts and revisions. Budget: Indicate your budget range for the project to attract designers who can provide high-quality work within your financial constraints. Responsive Designers: Request that designers are responsive to messages and able to make necessary revisions in a timely manner.
Nice to have
• Creative Elements: Incorporate unique and creative design elements that align with Vostrand's brand identity and the Commercial Real Estate industry. Texture or Embossing: If applicable and within budget, consider incorporating textured or embossed elements to add a tactile dimension to the stationery. Custom Illustrations: Include custom illustrations or graphics that convey the essence of the commercial real estate industry or your company's mission and values. Watermark or Background Pattern: Consider adding a subtle watermark or background pattern that complements the overall design without distracting from the content. Custom Typography: Explore the use of custom typography or stylized lettering for headers or key text elements to make the stationery more visually appealing. Enhanced Print Options: If budget allows, opt for premium printing techniques like foil stamping, spot UV, or letterpress to make the stationery truly stand out. Digital Templates: Request digital templates for electronic documents, such as Microsoft Word templates, PowerPoint templates, or PDF templates, to maintain consistency in digital communications. Multiple Design Concepts: Ask for variations of the stationery design to choose from, providing you with options for different occasions or purposes. QR Codes: If relevant, consider incorporating QR codes that link to Vostrand's website, portfolio, or contact information for convenient access. Environmentally Friendly Options: Explore eco-friendly printing materials and practices to align with sustainability goals, if applicable. Mobile Optimization: Ensure that any digital templates or elements are optimized for mobile use, enhancing accessibility and usability. Social Media Icons: Include social media icons and links to Vostrand's social media profiles, if desired, for a comprehensive online presence. Alternate Color Schemes: Request variations of the design with alternate color schemes for seasonal or special occasions.
Should not have
• Non-Compliance with Brand Guidelines: Specify that the design must strictly adhere to Vostrand's brand guidelines, and any deviations are not acceptable. Excessive Complexity: Avoid overly complex designs that may clutter the stationery or distract from the essential information. Inconsistent Branding: Ensure that all design elements, including colors, fonts, and logo usage, remain consistent with the provided brand standards. Unapproved Fonts: Specify that designers should only use the approved fonts from the brand guidelines and avoid introducing new fonts. Inappropriate Imagery: Request that designers refrain from using images, illustrations, or graphics that are unrelated to the Commercial Real Estate industry or that could potentially be perceived as unprofessional. Overly Bright Colors: If it doesn't align with your brand, discourage the use of overly bright or neon colors that may not convey professionalism. Clashing Color Schemes: Ensure that the color scheme chosen for the design is harmonious and avoids color combinations that clash or are difficult to read. Overuse of Effects: Discourage excessive use of visual effects, such as gradients, drop shadows, or excessive transparency, which can make the stationery appear cluttered. Extravagant Printing Costs: Specify that designers should consider budget constraints and avoid design elements that would significantly increase printing costs, unless the budget allows for premium printing techniques. Outdated Design Trends: Request that the design avoids incorporating outdated design trends that may make the stationery appear dated. Inconsistent Branding Across Items: Ensure that the design maintains consistency across all stationery items (letterhead, business cards, envelopes, etc.) and that there are no significant variations that could create confusion. Overly Busy Layouts: Ask for designs that have a clean and professional appearance, avoiding overcrowded layouts that make it difficult to read or find essential information.

```html
<!DOCTYPE html>
<html lang="en">
<head>
<meta charset="utf-8">
<title>Vostrand Letterhead</title>
<link rel="stylesheet" href="https://fonts.googleapis.com/css2?family=Roboto:wght@400;700&display=swap">
<style>
  :root {
    --backdrop: #e4e5e8;
    --paper: #ffffff;
    --navy: #0a1e4a;
    --accent-blue: #4a8fd0;
    --text-grey: #6b6b6b;
  }
  * { margin: 0; padding: 0; box-sizing: border-box; }
  html, body {
    width: 920px;
    height: 1200px;
    overflow: hidden;
    background: var(--backdrop);
    font-family: "Roboto", sans-serif;
  }
  .letterhead {
    position: absolute;
    left: 54px;
    top: 30px;
    width: 812px;
    height: 1140px;
    background: var(--paper);
  }
  .brand-name {
    position: absolute;
    left: 26px;
    top: 70px;
    font-size: 27px;
    font-weight: 700;
    letter-spacing: 3px;
    color: var(--navy);
    text-transform: uppercase;
  }
  .contact-list {
    position: absolute;
    right: 26px;
    top: 44px;
    list-style: none;
  }
  .contact-item {
    display: flex;
    justify-content: flex-end;
    align-items: center;
    gap: 5px;
    height: 20.5px;
    font-size: 12px;
    color: var(--text-grey);
  }
  .contact-icon {
    width: 14px;
    height: 14px;
    display: block;
  }
  .address-line {
    position: absolute;
    right: 26px;
    top: 1080px;
    display: flex;
    align-items: center;
    gap: 9px;
    font-size: 16px;
    color: var(--text-grey);
  }
  .pin-icon { width: 19px; height: 25px; display: block; }
  .footer-rule {
    position: absolute;
    left: 0;
    top: 1108px;
    width: 812px;
    height: 14px;
  }
</style>
</head>
<body>
  <main class="letterhead">
    <div class="brand-name">Vostrand</div>

    <ul class="contact-list">
      <li class="contact-item">
        <span>0147-582-316</span>
        <svg class="contact-icon" viewBox="0 0 14 14" aria-hidden="true">
          <rect width="14" height="14" rx="2" fill="var(--navy)"/>
          <path d="M4.2 3.2c.4-.3.9-.2 1.1.2l.7 1.3c.2.4.1.8-.2 1l-.5.4c.4.9 1.1 1.7 2 2.1l.4-.5c.3-.3.7-.4 1-.2l1.3.7c.4.2.5.7.2 1.1l-.5.6c-.4.5-1.1.6-1.7.4C6 9.6 4.3 7.9 3.6 5.9c-.2-.6 0-1.3.4-1.7z" fill="#fff"/>
        </svg>
      </li>
      <li class="contact-item">
        <span>info@vostrandrealty.com</span>
        <svg class="contact-icon" viewBox="0 0 14 14" aria-hidden="true">
          <rect width="14" height="14" rx="2" fill="var(--navy)"/>
          <rect x="2.5" y="4" width="9" height="6.2" fill="none" stroke="#fff" stroke-width="1"/>
          <path d="M2.5 4l4.5 3.4L11.5 4M2.5 10.2l3.4-3M11.5 10.2l-3.4-3" fill="none" stroke="#fff" stroke-width="0.9"/>
        </svg>
      </li>
      <li class="contact-item">
        <span>vostrandrealty.com</span>
        <svg class="contact-icon" viewBox="0 0 14 14" aria-hidden="true">
          <rect width="14" height="14" rx="2" fill="var(--navy)"/>
          <path d="M5 3.2v7.2l1.7-1.6 1.2 2.6 1.1-.5-1.2-2.5h2.3z" fill="#fff"/>
        </svg>
      </li>
    </ul>

    <div class="address-line">
      <span>4180 Meridian Park Ln. Suite Austin, TX 0000</span>
      <svg class="pin-icon" viewBox="0 0 19 25" aria-hidden="true">
        <ellipse cx="9.5" cy="21.5" rx="8" ry="2.6" fill="none" stroke="var(--accent-blue)" stroke-width="1.6"/>
        <path d="M9.5 1C5.6 1 3 3.9 3 7.3c0 4.4 6.5 13 6.5 13S16 11.7 16 7.3C16 3.9 13.4 1 9.5 1z" fill="var(--accent-blue)"/>
        <circle cx="9.5" cy="7.3" r="2.6" fill="#fff"/>
      </svg>
    </div>

    <svg class="footer-rule" viewBox="0 0 812 14" aria-hidden="true">
      <polygon points="0,2 375,2 389,14 0,14" fill="var(--navy)"/>
      <rect x="389" y="7" width="423" height="1" fill="var(--accent-blue)"/>
    </svg>
  </main>
</body>
</html>
```